ラベルのイメ―ジ
・高級感
・安心感
・品質(GMP認定工場による生産)

※KAIROの化学式や、DNA螺旋などをイメージするようなイラストも良いと考えています。必須ではありません。

ターゲット層は以下を想定しています
性別:どちらもあると考えていますが、パッケージラベルは男性向けと想定しています
収入:余裕のある方
年齢:30-60歳
サイズ:W65㎜×H80㎜
カラー:黒字にゴールド
赤系、青系、無彩色系、ゴールド
写真のパッケージは、白ですが、実物は同じ物の黒を想定しています。ファイル「ラベルのサンプル画像.jpg」は、他社製品で、イメージの近いものを選んでいます。

要件をそろえたすばらしいデザインです。
ありがとうございます。

この度は、多くの方よりご提案をいただきました。まことにありがとうございます。
今後も新製品や、製品説明資料などでおご依頼の機会が有るかと思います。
その際もよろしくお願いします。

```html
<!DOCTYPE html>
<html lang="ja">
<head>
<meta charset="UTF-8">
<title>KAIRO Label</title>
<link rel="stylesheet" href="https://fonts.googleapis.com/css2?family=Cinzel:wght@600&family=Noto+Serif+JP:wght@500&family=Cormorant+Garamond:ital,wght@1,500&display=swap">
<style>
  :root {
    --bg: #ffffff;
    --label-black: #0b0b0b;
    --gold-light: #f3d98a;
    --gold-mid: #c9a24a;
    --gold-dark: #8a6a22;
    --gold-text: #d6b25e;
  }
  html, body {
    margin: 0;
    padding: 0;
    width: 846px;
    height: 1200px;
    overflow: hidden;
    background: var(--bg);
  }
  .canvas {
    position: relative;
    width: 846px;
    height: 1200px;
  }
  .label {
    position: absolute;
    left: 73px;
    top: 169px;
    width: 700px;
    height: 862px;
    background: var(--label-black);
    overflow: hidden;
  }
  .label__ornament {
    position: absolute;
    left: 30px;
    top: 36px;
    width: 640px;
    height: 172px;
    background: linear-gradient(180deg, var(--gold-mid) 0%, var(--gold-dark) 100%);
    opacity: 0.85;
  }
  .label__tagline {
    position: absolute;
    left: 0;
    top: 290px;
    width: 700px;
    margin: 0;
    text-align: center;
    font-family: "Noto Serif JP", serif;
    font-weight: 500;
    font-size: 24px;
    letter-spacing: 0.2em;
    color: var(--gold-text);
  }
  .label__name {
    position: absolute;
    left: 0;
    top: 350px;
    width: 700px;
    margin: 0;
    text-align: center;
    font-family: "Cinzel", serif;
    font-weight: 600;
    font-size: 150px;
    line-height: 1;
    letter-spacing: 0.02em;
    color: var(--gold-text);
  }
  .label__molecule {
    position: absolute;
    left: 300px;
    top: 590px;
    width: 100px;
    height: 90px;
    background: linear-gradient(180deg, var(--gold-mid), var(--gold-dark));
    border-radius: 6px;
  }
  .label__quality {
    position: absolute;
    left: 0;
    top: 780px;
    width: 700px;
    margin: 0;
    text-align: center;
    font-family: "Cormorant Garamond", serif;
    font-style: italic;
    font-weight: 500;
    font-size: 26px;
    color: var(--gold-text);
  }
</style>
</head>
<body>
<main class="canvas">
  <section class="label">
    <div class="label__ornament" role="img" aria-label="Gold decorative header ornament"></div>
    <p class="label__tagline">永く輝く</p>
    <h1 class="label__name">KAIRO</h1>
    <div class="label__molecule" role="img" aria-label="Small molecular structure motif"></div>
    <p class="label__quality">High Quality</p>
  </section>
</main>
</body>
</html>
```